Antigen Preservation Center

The company will provide a contract research services to stabilize various viruses, viral vectors, and vaccines. It may offer some licensing opportunities for stabilizing technologies. Main area of applications are pharmaceutical, therapeutic, and vaccination field. The company aspires to develop room temperature vaccines for global distribution beyond the current cold chain.
Updates

Target Market(s)

pharmaceutical, therapeutic and vaccination fields

Coding

Number of Pages Required

4 page

Requirements
Must have
• Incorporate a APC logo, attached at the bottom, on the Web page

```html
<!DOCTYPE html>
<html lang="en">
<head>
<meta charset="utf-8">
<title>Antigen Preservation Center</title>
<link href="https://fonts.googleapis.com/css2?family=Raleway:ital,wght@0,300;0,400;0,500;0,600;0,700;1,300;1,400&display=swap" rel="stylesheet">
<style>
:root{
  --green:#4f9e7c;
  --green-dark:#3f8a69;
  --gold:#c99a45;
  --gold-band:#d2a24c;
  --ink:#222;
  --muted:#6b6b6b;
  --line:#e4e4e4;
  --paper:#f6f6f4;
  --white:#fff;
}
*{box-sizing:border-box;margin:0;padding:0}
html,body{width:1200px;height:2946px;overflow:hidden}
body{font-family:"Raleway",sans-serif;color:var(--ink);background:var(--white);position:relative}
.abs{position:absolute}
.ph{position:absolute}

/* header */
.site-header{position:absolute;left:0;top:0;width:1200px;height:63px;background:var(--white);border-bottom:1px solid var(--line)}
.brand{position:absolute;left:137px;top:13px;display:flex;align-items:center;gap:10px}
.brand-mark{width:36px;height:36px;border-radius:50%;background:var(--green)}
.brand-name{font-size:12px;font-weight:600;letter-spacing:2px;line-height:1.2;color:var(--green-dark);text-transform:uppercase;width:150px}
.main-nav{position:absolute;left:524px;top:0;display:flex;gap:0;height:63px}
.main-nav a{font-size:13px;color:#333;text-decoration:none;width:88px;line-height:63px;text-align:center}
.main-nav a.active{color:var(--gold);border-top:3px solid var(--gold);line-height:57px}

/* hero */
.hero{position:absolute;left:0;top:63px;width:1200px;height:538px;background:linear-gradient(100deg,#4a9a78 0%,#6aa98a 45%,#579f80 100%)}
.hero-quote{position:absolute;left:161px;top:160px;width:520px;font-size:34px;font-weight:300;font-style:italic;color:var(--white);line-height:1.3}
.hero-quote span{font-style:normal;color:#cfe3d8}
.hero-rule{position:absolute;left:161px;top:255px;width:34px;height:1px;background:#cfe3d8}
.hero-sub{position:absolute;left:161px;top:275px;width:300px;font-size:17px;color:var(--white);line-height:1.35}
.contact-card{position:absolute;left:756px;top:78px;width:310px;height:362px;background:var(--white);box-shadow:0 2px 8px rgba(0,0,0,.2);padding:26px 38px}
.contact-card h3{font-size:16px;font-weight:500;text-align:center}
.contact-card .hint{font-size:10px;text-align:center;color:var(--muted);margin-top:4px}
.field{height:30px;border:1px solid var(--line);margin-top:14px;font-size:9px;color:#999;padding:9px 8px}
.field.focus{border-color:#7fb3e0;margin-top:22px}
.consent{font-size:7.5px;color:var(--muted);line-height:1.5;margin-top:14px}
.btn-gold{margin-top:14px;height:34px;background:var(--gold);color:var(--white);font-size:12px;font-weight:600;text-align:center;line-height:34px}

/* intro */
.intro-photo{left:0;top:601px;width:436px;height:283px;background:linear-gradient(135deg,#d8d6d0,#b39a86 55%,#e6e6e2)}
.intro-text{position:absolute;left:560px;top:655px;width:492px;font-size:12.5px;line-height:2.2;color:var(--muted)}
.intro-text b,.feature-text b{color:var(--ink);font-weight:700}

/* applications */
.applications{position:absolute;left:0;top:884px;width:1200px;height:456px;background:var(--paper)}
.section-title{position:absolute;width:1200px;text-align:center;font-size:22px;font-weight:400}
.title-rule{position:absolute;left:570px;width:60px;height:2px;background:#555}
.app-card{position:absolute;top:133px;width:242px;height:234px;background:var(--white);border:1px solid var(--line);text-align:center;padding-top:30px}
.num{width:46px;height:46px;border:2px dashed var(--green-dark);border-radius:50%;margin:0 auto;font-size:26px;line-height:42px;color:var(--green-dark)}
.app-card h4{font-size:16px;font-weight:500;margin-top:10px}
.app-card p{font-size:9.5px;line-height:1.5;color:#444;margin:8px 28px 0}
.read-more{display:block;font-size:9px;color:var(--gold);font-weight:600;margin-top:26px}

/* gold band */
.statement{position:absolute;left:0;top:1340px;width:1200px;height:257px;background:var(--gold-band);text-align:center;color:var(--white)}
.statement .qmark{font-size:34px;font-weight:700;margin-top:40px;line-height:1}
.statement p{font-size:21px;line-height:1.45;margin:22px auto 0;width:700px;font-weight:300}
.statement b{font-weight:600}

/* testimonials */
.testimonials{position:absolute;left:0;top:1597px;width:1200px;height:446px;background:var(--paper);overflow:hidden}
.t-card{position:absolute;top:137px;width:330px;height:242px;background:var(--white);box-shadow:0 1px 5px rgba(0,0,0,.15)}
.t-photo{left:0;top:0;width:152px;height:242px}
.t-body{position:absolute;left:172px;top:22px;width:146px;font-size:9.5px;font-style:italic;line-height:1.75;color:#333}
.t-name{position:absolute;left:172px;top:208px;font-size:10px;font-weight:700}
.t-quote{position:absolute;right:12px;bottom:6px;font-size:24px;font-weight:700;color:var(--gold)}

/* feature */
.feature-title{position:absolute;left:114px;top:2133px;font-size:22px;font-weight:400}
.feature-rule{position:absolute;left:114px;top:2176px;width:34px;height:2px;background:#555}
.feature-text{position:absolute;left:114px;top:2210px;width:500px;font-size:12.5px;line-height:2.2;color:var(--muted)}
.feature-photo{left:707px;top:2131px;width:365px;height:249px;background:linear-gradient(120deg,#e9ecec,#c9b19c 60%,#f1f1ef);box-shadow:0 2px 8px rgba(0,0,0,.25);border:5px solid var(--white)}

/* footer */
.site-footer{position:absolute;left:0;top:2461px;width:1200px;height:485px;background:linear-gradient(100deg,#4a9a78,#65a787 50%,#4f9e7c)}
.site-footer .section-title{top:54px;color:var(--white)}
.site-footer .title-rule{top:94px;background:#d9ece2}
.contact-item{position:absolute;top:124px;width:200px;text-align:center;color:var(--white);font-size:11px}
.contact-item svg{display:block;margin:0 auto 10px}
.f-field{position:absolute;background:rgba(255,255,255,.22);color:var(--white);font-size:11px;font-weight:600;padding:11px 14px}
.footer-nav{position:absolute;left:250px;top:2886px;width:700px;display:flex;justify-content:center;gap:30px;font-size:10px;font-weight:600;color:var(--white);border-bottom:1px solid rgba(255,255,255,.5);padding-bottom:10px}
.legal{position:absolute;left:0;top:2916px;width:1200px;text-align:center;font-size:8px;color:var(--white);font-weight:600}
</style>
</head>
<body>

<header class="site-header">
  <div class="brand"><span class="brand-mark"></span><span class="brand-name">Antigen Preservation Center</span></div>
  <nav class="main-nav">
    <a>About us</a><a class="active">Services</a><a>Compliances</a><a>Expertise</a><a>Resources</a><a>Contacts</a>
  </nav>
</header>

<section class="hero" role="img" aria-label="Photo of a smiling woman and man, green tinted">
  <p class="hero-quote">“The groundwork of all happ ness is good health”<span>– Elise Hartwell</span></p>
  <div class="hero-rule"></div>
  <p class="hero-sub">Get in touch with usand we will be ready to answer any question.</p>
  <form class="contact-card">
    <h3>Get in Touch With Us</h3>
    <p class="hint">Fill the information below</p>
    <div class="field focus">First Name</div>
    <div class="field">Last Name</div>
    <div class="field">Email Address</div>
    <div class="field">Phone Number</div>
    <p class="consent">By clicking Join now, you agree to the site's terms of use, Privacy Policy and Cookie Policy.</p>
    <div class="btn-gold">Send Request</div>
  </form>
</section>

<div class="ph intro-photo" role="img" aria-label="Portrait photo of a smiling man"></div>
<p class="intro-text"><b>Lorem ipsum dolor sit amet, consectetuer adipiscing elit. Aenean commodo ligula eget dolor. Aenean massa.</b> Cum sociis natoque penatibus et magnis dis parturient montes, nascetur ridiculus mus. Donec quam felis, ultricies nec, pellentesque eu, pretium quis, sem. Nulla consequat massa quis enim. Donec pede justo, fringilla vel, aliquet nec, vulputate eget, arcu. In enim justo, rhoncus ut, imperdiet a, venenatis vitae, justo. Nullam dictum</p>

<section class="applications">
  <h2 class="section-title" style="top:62px">Main Area of Applications</h2>
  <div class="title-rule" style="top:102px"></div>
  <div class="app-card" style="left:206px"><div class="num">1</div><h4>Pharmaceutical</h4><p>Lorem ipsum dolor sit amet, consectetuer adipiscing elit. Aenean commodo ligula eget dolor</p><span class="read-more">Read more</span></div>
  <div class="app-card" style="left:465px"><div class="num">2</div><h4>Therapeutical</h4><p>Lorem ipsum dolor sit amet, consectetuer adipiscing elit. Aenean commodo ligula eget dolor.</p><span class="read-more">Read more</span></div>
  <div class="app-card" style="left:725px"><div class="num">3</div><h4>Vaccination</h4><p>Lorem ipsum dolor sit amet, consectetuer adipiscing elit. Aenean commodo ligula eget dolor</p><span class="read-more">Read more</span></div>
</section>

<section class="statement">
  <div class="qmark">“</div>
  <p><b>We indirectly contribute</b> to maximizing our client's revenue quotients, streamlining their operations and thus aid in advancing their existing potentials and businesses.</p>
</section>

<section class="testimonials">
  <h2 class="section-title" style="top:50px">Company Leaders Testimonials</h2>
  <div class="title-rule" style="top:90px"></div>
  <div class="t-card" style="left:-282px"><span class="t-quote">“</span></div>
  <div class="t-card" style="left:79px"><div class="ph t-photo" role="img" aria-label="Photo of a smiling man in a denim shirt" style="background:linear-gradient(160deg,#8a7664,#5b6f86)"></div><p class="t-body">Lorem ipsum dolor sit amet, consectetuer adipiscing elit. Aenean commodo ligula eget dolor. Aenean massa. Cum sociis natoque penatibus et magnis dis parturient montes, nascetur ridiculus mus. Donec quam felis, ultricies nec</p><span class="t-name">- Mark Dellan</span><span class="t-quote">“</span></div>
  <div class="t-card" style="left:440px"><div class="ph t-photo" role="img" aria-label="Photo of a man in a suit" style="background:linear-gradient(160deg,#b8aba0,#3a3f48)"></div><p class="t-body">Lorem ipsum dolor sit amet, consectetuer adipiscing elit. Aenean commodo ligula eget dolor. Aenean massa. Cum sociis natoque penatibus et magnis dis parturient montes, nascetur ridiculus mus. Donec quam felis, ultricies nec, pellentesque eu, pretium.</p><span class="t-name">- Mark Dellan</span><span class="t-quote">“</span></div>
  <div class="t-card" style="left:799px"><div class="ph t-photo" role="img" aria-label="Photo of a smiling man in a checked shirt" style="background:linear-gradient(160deg,#a58a74,#4d6a7e)"></div><p class="t-body">Lorem ipsum dolor sit amet, consectetuer adipiscing elit. Aenean commodo ligula eget dolor. Aenean massa. Cum sociis natoque penatibus et magnis dis parturient montes, nascetur ridiculus mus. Donec quam felis, ultricies nec</p><span class="t-name">- Mark Dellan</span><span class="t-quote">“</span></div>
  <div class="t-card" style="left:1159px"><div class="ph t-photo" role="img" aria-label="Photo of a man" style="background:linear-gradient(160deg,#8d7a68,#4e5a66)"></div></div>
</section>

<h2 class="feature-title">Section Headline</h2>
<div class="feature-rule"></div>
<p class="feature-text"><b>Lorem ipsum dolor sit amet, consectetuer adipiscing elit. Aenean commodo ligula eget dolor. Aenean massa.</b> Cum sociis natoque penatibus et magnis dis parturient montes, nascetur ridiculus mus. Donec quam felis, ultricies nec, pellentesque eu, pretium quis, sem. Nulla consequat massa quis enim. Donec pede justo, fringilla vel, aliquet nec, vulputate eget, arcu.</p>
<div class="ph feature-photo" role="img" aria-label="Photo of a dentist in a clinic"></div>

<footer class="site-footer" role="img" aria-label="Photo of a smiling woman, green tinted">
  <h2 class="section-title">Get in Touch</h2>
  <div class="title-rule"></div>
  <div class="contact-item" style="left:315px">
    <svg width="18" height="24" viewBox="0 0 18 24"><path d="M9 0C4 0 0 4 0 9c0 6 9 15 9 15s9-9 9-15c0-5-4-9-9-9zm0 12a3 3 0 110-6 3 3 0 010 6z" fill="#fff"/></svg>
    2210 N Your full address</div>
  <div class="contact-item" style="left:505px">
    <svg width="22" height="24" viewBox="0 0 22 24"><rect x="1" y="6" width="20" height="14" fill="#fff"/><path d="M1 6l10 8 10-8" stroke="#4f9e7c" stroke-width="1.5" fill="none"/></svg>
    support@northfieldhealth.org</div>
  <div class="contact-item" style="left:678px">
    <svg width="20" height="24" viewBox="0 0 20 24"><path d="M4 3l4 0 2 5-3 2c1 3 3 5 6 6l2-3 5 2v4c-9 1-17-7-16-16z" fill="#fff"/></svg>
    (555) 210 - 0348</div>
  <div class="f-field" style="left:226px;top:212px;width:363px;height:37px">Name</div>
  <div class="f-field" style="left:226px;top:273px;width:363px;height:37px">Email</div>
  <div class="f-field" style="left:226px;top:334px;width:363px;height:37px">Subject</div>
  <div class="f-field" style="left:609px;top:212px;width:363px;height:159px">Message</div>
</footer>
<nav class="footer-nav"><span>About us</span><span>Services</span><span>Compliances</span><span>Expertise</span><span>Resources</span><span>IT services &amp; solutions</span><span>Contacts</span></nav>
<p class="legal">All rights reserved &nbsp;|&nbsp; Privacy Policy &nbsp;|&nbsp; Terms</p>

</body>
</html>
```